KRMTOP - Harwell Clerical Solutions, Inc./Pinecrest Mailing Works, Inc. Needs a Letterhead Desig

Letterhead - thoughts 2 files uploaded 1 is the current letterhead and only change to the words is message at bottom - should be 25 Years of Industry Experience

2nd file is so that you can see how top of letterhead was before changes - had graphic bleed which we liked.

Goal for letterhead - we're a print / mail shop so we need a look that fits with agencies. I would like a bit of a square font for address, phone, email info otherwise be creative. We like a blue 307 and would like to incorporate a little green or tan.

```html
<!DOCTYPE html>
<html lang="en">
<head>
<meta charset="utf-8">
<title>KRMTOP Letterhead</title>
<link href="https://fonts.googleapis.com/css2?family=Questrial&family=Oswald:wght@500&family=Michroma&display=swap" rel="stylesheet">
<style>
  :root {
    --blue: #1d5aa6;
    --blue-dark: #0f4f94;
    --green: #1fa35b;
    --ink: #444a52;
    --paper: #f6f6f6;
    --swoosh: #e6e6e6;
    --backdrop: #d9d9d9;
    --rule: #c9c9c9;
  }
  * { box-sizing: border-box; margin: 0; padding: 0; }
  html, body { width: 1200px; height: 900px; overflow: hidden; }
  body { background: var(--backdrop); font-family: "Questrial", sans-serif; color: var(--ink); position: relative; }

  .sheet { position: absolute; top: 92px; width: 506px; height: 715px; background: var(--paper); overflow: hidden; }
  .sheet--letter { left: 72px; }
  .sheet--blank { left: 631px; }

  .sheet__swoosh { position: absolute; left: 0; top: 0; width: 506px; height: 120px; }

  .brand { position: absolute; left: 48px; top: 36px; display: flex; gap: 14px; }
  .brand__unit { display: flex; flex-direction: column; }
  .brand__name { font-family: "Michroma", sans-serif; font-size: 22px; line-height: 24px; color: var(--blue); letter-spacing: 2px; }
  .brand__sub { font-size: 4.6px; color: var(--blue); text-transform: uppercase; letter-spacing: 0.2px; margin-top: 1px; white-space: nowrap; }

  .fold { position: absolute; left: 0; width: 22px; height: 1px; background: var(--rule); }

  .letter { position: absolute; left: 47px; top: 154px; width: 415px; font-size: 7.4px; line-height: 9.2px; }
  .letter__date { margin-bottom: 10px; }
  .letter__address { margin-bottom: 28px; }
  .letter__salutation { font-weight: bold; margin-bottom: 9px; }
  .letter__body p { text-align: justify; margin-bottom: 9px; }
  .letter__signer { font-weight: bold; font-size: 6.6px; margin-top: 10px; letter-spacing: 0.2px; }
  .letter__signature { width: 110px; height: 30px; margin-top: 6px; margin-left: -6px; background: linear-gradient(90deg, rgba(40,60,170,0.18), rgba(40,60,170,0.05)); }

  .footer { position: absolute; left: 23px; top: 674px; width: 460px; height: 26px; font-size: 7.4px; line-height: 9.5px; }
  .footer__address { position: absolute; left: 0; top: 8px; }
  .footer__col { position: absolute; top: 8px; padding-left: 6px; border-left: 1px solid var(--rule); }
  .footer__col--phone { left: 86px; }
  .footer__col--web { left: 158px; }
  .footer__item { display: flex; align-items: center; gap: 4px; white-space: nowrap; }
  .footer__item svg { width: 7px; height: 7px; flex: none; }
  .footer__tagline { position: absolute; left: 296px; top: 4px; width: 156px; font-family: "Oswald", sans-serif; font-weight: 500; font-size: 12.5px; line-height: 14px; color: var(--blue); letter-spacing: -0.2px; white-space: nowrap; padding-bottom: 3px; border-bottom: 3.6px solid var(--green); }

  .sheet__band { position: absolute; left: 0; bottom: 0; width: 100%; height: 9px; background: var(--blue-dark); }
</style>
</head>
<body>

<section class="sheet sheet--letter">
  <svg class="sheet__swoosh" viewBox="0 0 506 120" aria-hidden="true">
    <path d="M262 98 C360 82 450 45 506 0 L506 0 L506 10 C470 55 380 88 262 98 Z" fill="var(--swoosh)"/>
  </svg>
  <header class="brand">
    <div class="brand__unit"><span class="brand__name">KRM</span><span class="brand__sub">Harwell Clerical Solutions, Inc.</span></div>
    <div class="brand__unit"><span class="brand__name">TOP</span><span class="brand__sub">Pinecrest Mailing Works, Inc.</span></div>
  </header>

  <span class="fold" style="top:252px"></span>
  <span class="fold" style="top:506px"></span>

  <article class="letter">
    <p class="letter__date">30.02.2015</p>
    <p class="letter__address">Recipient's name<br>Lindenweg 4<br>20095 Hamburg<br>Germany</p>
    <p class="letter__salutation">Dear sir,</p>
    <div class="letter__body">
      <p>Communication is a very integral part of living creatures, animals and humans. Communication may be verbal or written. Written communication however is only applicable to human beings. Can you even imagine a world without communication? Verbal communication can be through telephones, webcams or in person. Written communication is through letters, emails and mobile phone messages.</p>
      <p>In today's world of great inventions and technology, letters have somehow become redundant. It is the time for text messages or chats. But they still can communicate a lot more than all other modes of communication. Organizations and various government departments still bank on letters as a strong medium of communication. There is no comparison in costs of sending letters as compared to costs of mobile phone messages though – letters are far cheaper. Letters now commonly known as "hard copy documents" are considered more relevant and important than email copies of text messages as proof or evidence of some sort.</p>
      <p>Letters speak volumes about a person or an organization that writes it. So one must take utmost care ensuring that the language used in any letter is appropriate for the occasion for which it is being written. Since a letter is also a written proof or document, if there are certain things that should not form a part of it, then that too should be carefully handled.</p>
      <p>Writing a good letter is an art. But if for some reason someone is unable to write that perfect letter, these different types of letters provide a base for you to build on. Sample letters have been given for everyone to understand what all information needs to form a part of the letter type and then it can be customized.</p>
    </div>
    <p class="letter__signer">Dr. Dr. MARTEN VOSS</p>
    <div class="letter__signature" role="img" aria-label="Handwritten signature in blue ink"></div>
  </article>

  <footer class="footer">
    <p class="footer__address">4120 W. Halden Ave<br>Oakmere, IL 60512</p>
    <div class="footer__col footer__col--phone">
      <p class="footer__item"><svg viewBox="0 0 8 8"><rect width="8" height="8" rx="1.5" fill="var(--blue)"/><path d="M2.3 1.8c.4 1.9 1.6 3.3 3.7 4.2l.6-.9-1-.6-.5.5C4.2 4.6 3.6 4 3.2 3.1l.5-.5-.6-1z" fill="#fff"/></svg>555-214-3380</p>
      <p class="footer__item"><svg viewBox="0 0 8 8"><rect width="8" height="8" rx="1.5" fill="var(--blue)"/><rect x="2" y="2" width="4" height="1.6" fill="#fff"/><rect x="1.6" y="4.2" width="4.8" height="2.2" fill="#fff"/></svg>555-214-3391</p>
    </div>
    <div class="footer__col footer__col--web">
      <p class="footer__item"><svg viewBox="0 0 8 8"><rect width="8" height="8" rx="1.5" fill="var(--blue)"/><rect x="1.6" y="2.4" width="4.8" height="3.2" fill="none" stroke="#fff" stroke-width=".7"/><path d="M1.6 2.4 4 4.4 6.4 2.4" fill="none" stroke="#fff" stroke-width=".7"/></svg>service@krmtop.com</p>
      <p class="footer__item"><svg viewBox="0 0 8 8"><rect width="8" height="8" rx="1.5" fill="var(--blue)"/><circle cx="4" cy="4" r="2.3" fill="none" stroke="#fff" stroke-width=".7"/><path d="M1.7 4h4.6" stroke="#fff" stroke-width=".6"/></svg>www.krmtop.com</p>
    </div>
    <p class="footer__tagline">25 YEARS OF INDUSTRY EXPERIENCE</p>
  </footer>
  <div class="sheet__band"></div>
</section>

<section class="sheet sheet--blank">
  <svg class="sheet__swoosh" viewBox="0 0 506 120" aria-hidden="true">
    <path d="M262 98 C360 82 450 45 506 0 L506 0 L506 10 C470 55 380 88 262 98 Z" fill="var(--swoosh)"/>
  </svg>
  <header class="brand">
    <div class="brand__unit"><span class="brand__name">KRM</span><span class="brand__sub">Harwell Clerical Solutions, Inc.</span></div>
    <div class="brand__unit"><span class="brand__name">TOP</span><span class="brand__sub">Pinecrest Mailing Works, Inc.</span></div>
  </header>

  <footer class="footer">
    <p class="footer__address">4120 W. Halden Ave<br>Oakmere, IL 60512</p>
    <div class="footer__col footer__col--phone">
      <p class="footer__item"><svg viewBox="0 0 8 8"><rect width="8" height="8" rx="1.5" fill="var(--blue)"/><path d="M2.3 1.8c.4 1.9 1.6 3.3 3.7 4.2l.6-.9-1-.6-.5.5C4.2 4.6 3.6 4 3.2 3.1l.5-.5-.6-1z" fill="#fff"/></svg>555-214-3380</p>
      <p class="footer__item"><svg viewBox="0 0 8 8"><rect width="8" height="8" rx="1.5" fill="var(--blue)"/><rect x="2" y="2" width="4" height="1.6" fill="#fff"/><rect x="1.6" y="4.2" width="4.8" height="2.2" fill="#fff"/></svg>555-214-3391</p>
    </div>
    <div class="footer__col footer__col--web">
      <p class="footer__item"><svg viewBox="0 0 8 8"><rect width="8" height="8" rx="1.5" fill="var(--blue)"/><rect x="1.6" y="2.4" width="4.8" height="3.2" fill="none" stroke="#fff" stroke-width=".7"/><path d="M1.6 2.4 4 4.4 6.4 2.4" fill="none" stroke="#fff" stroke-width=".7"/></svg>service@krmtop.com</p>
      <p class="footer__item"><svg viewBox="0 0 8 8"><rect width="8" height="8" rx="1.5" fill="var(--blue)"/><circle cx="4" cy="4" r="2.3" fill="none" stroke="#fff" stroke-width=".7"/><path d="M1.7 4h4.6" stroke="#fff" stroke-width=".6"/></svg>www.krmtop.com</p>
    </div>
    <p class="footer__tagline">25 YEARS OF INDUSTRY EXPERIENCE</p>
  </footer>
  <div class="sheet__band"></div>
</section>

</body>
</html>
```